Vietnam Recruitment Tour Postcard

We need a postcard to market a U.S. university student recruitment tour in northern Vietnam. The fair tour is organized by StudyBridgeAbroad which is a program of the Federal Office of Exchange www.studybridgeabroad.exchange-office.example

The audience for these postcards are U.S. higher education recruiters (not students). We want U.S. universities to sign up for the fair tour.

The postcards will be handed out at large education conferences.

Target Market(s)

U.S. university recruiters who are between the ages of 25 and 45.

Industry/Entity Type

University

Requirements
Must have
• Copy/Text: Please see attached doc. file for copy/text to be used on the front and back of the card.

Front: High color gloss

Back: Black and white only design

Featured Colors: Red, White, and Blue
- Should have a patriotic / U.S. government feel

Logos: Must use the attached Exchange Office logo and at least one StudyBridgeAbroad logo (can use more but not required)

```html
<!DOCTYPE html>
<html lang="en">
<head>
<meta charset="utf-8">
<title>Off The Beaten Track Tour – Postcard</title>
<link href="https://fonts.googleapis.com/css2?family=Arvo:wght@700&family=Roboto:wght@300;400;700;900&family=Roboto+Condensed:wght@400&display=swap" rel="stylesheet">
<style>
  :root {
    --page-bg-light: #f4f4f4;
    --page-bg-dark: #8a8a8a;
    --card-black: #050505;
    --flag-red: #b3121f;
    --flag-blue: #1c2a5c;
    --accent-red: #d7262b;
    --silver-light: #f2f2f2;
    --silver-dark: #8d8d8d;
    --text-grey: #b5b5b5;
    --date-grey: #7d7d7d;
    --white: #ffffff;
    --ink: #111111;
  }
  * { margin: 0; padding: 0; box-sizing: border-box; }
  html, body { width: 1200px; height: 1000px; overflow: hidden; }
  body {
    position: relative;
    font-family: "Roboto", Arial, sans-serif;
    background: linear-gradient(125deg, var(--page-bg-light) 0%, #d6d6d6 30%, var(--page-bg-dark) 60%, #cfcfcf 85%, var(--page-bg-light) 100%);
  }
  .sheet-title {
    position: absolute; left: 44px; top: 30px;
    font-family: "Roboto", Arial, sans-serif; font-weight: 900;
    font-size: 31px; color: var(--ink); letter-spacing: -0.5px;
  }
  .sheet-size {
    position: absolute; left: 44px; top: 68px;
    font-size: 16px; font-weight: 400; color: var(--ink);
  }

  /* Front */
  .card-front {
    position: absolute; left: 461px; top: 24px; width: 612px; height: 473px;
    background: var(--card-black); overflow: hidden;
    box-shadow: 0 2px 6px rgba(0,0,0,0.35);
  }
  .flag-photo {
    position: absolute; left: 0; top: 0; width: 612px; height: 330px;
    background:
      radial-gradient(ellipse 70% 60% at 10% 20%, rgba(40,55,110,0.95) 0%, rgba(28,42,92,0.6) 45%, transparent 75%),
      radial-gradient(ellipse 60% 55% at 55% 10%, rgba(179,18,31,0.95) 0%, rgba(140,15,25,0.5) 50%, transparent 80%),
      linear-gradient(180deg, transparent 40%, var(--card-black) 100%);
  }
  .light-beam {
    position: absolute; left: 312px; top: 0; width: 3px; height: 330px;
    background: linear-gradient(180deg, rgba(255,230,170,0.95), rgba(255,190,90,0.5) 60%, transparent);
    box-shadow: 0 0 14px 4px rgba(255,200,120,0.35);
  }
  .brand-mark {
    position: absolute; left: 30px; top: 50px;
    display: flex; align-items: center; gap: 8px;
    font-family: "Roboto", Arial, sans-serif; font-weight: 400;
    font-size: 24px; color: var(--white);
  }
  .brand-mark .dot { width: 12px; height: 12px; background: var(--white); border-radius: 50%; }
  .partner-mark {
    position: absolute; right: 28px; top: 18px; width: 130px;
    display: flex; flex-direction: column; align-items: center; gap: 6px;
    font-size: 12px; font-weight: 400; color: var(--white); text-align: center;
  }
  .partner-mark .circle {
    width: 120px; height: 120px; border-radius: 50%; background: var(--flag-blue);
  }
  .tour-title {
    position: absolute; left: 0; top: 198px; width: 100%;
    text-align: center; font-family: "Arvo", Georgia, serif; font-weight: 700;
    font-size: 35px; line-height: 44px;
    background: linear-gradient(180deg, var(--silver-light) 0%, #c9c9c9 50%, var(--silver-dark) 100%);
    -webkit-background-clip: text; background-clip: text; color: transparent;
  }
  .tour-invite {
    position: absolute; left: 0; top: 333px; width: 100%; text-align: center;
    font-weight: 700; font-size: 30px; color: var(--accent-red);
  }
  .tour-dates {
    position: absolute; left: 0; top: 370px; width: 100%; text-align: center;
    font-weight: 900; font-size: 20px; color: var(--date-grey);
  }
  .tour-dates b { color: var(--white); font-weight: 900; }
  .tour-note {
    position: absolute; left: 0; top: 412px; width: 100%; text-align: center;
    font-weight: 300; font-size: 18px; color: var(--text-grey);
  }
  .tour-signup {
    position: absolute; left: 0; top: 438px; width: 100%; text-align: center;
    font-weight: 300; font-size: 15px; color: var(--text-grey);
  }
  .tour-signup b { font-weight: 700; }

  /* Back */
  .card-back {
    position: absolute; left: 461px; top: 507px; width: 612px; height: 475px;
    background: var(--white); box-shadow: 0 2px 6px rgba(0,0,0,0.3);
  }
  .back-band {
    position: absolute; left: 0; top: 0; width: 461px; height: 153px;
    background: var(--card-black); overflow: hidden; color: var(--white);
  }
  .band-flag {
    position: absolute; left: 0; top: 0; width: 461px; height: 153px;
    background:
      radial-gradient(ellipse 50% 70% at 5% 30%, rgba(120,120,120,0.7), transparent 70%),
      radial-gradient(ellipse 40% 60% at 50% 0%, rgba(90,90,90,0.6), transparent 70%);
  }
  .band-content { position: absolute; left: 15px; top: 12px; right: 10px; }
  .save-title { font-weight: 900; font-size: 19px; line-height: 22px; }
  .save-lead { font-weight: 700; font-size: 10.5px; line-height: 13px; margin-top: 1px; width: 360px; }
  .save-meta { font-family: "Roboto Condensed", Arial, sans-serif; font-size: 9px; margin-top: 5px; color: #e0e0e0; }
  .schedule {
    position: absolute; top: 87px; font-family: "Roboto Condensed", Arial, sans-serif;
    font-size: 9.5px; line-height: 13px; border-collapse: collapse;
  }
  .schedule td { padding: 0; vertical-align: top; }
  .schedule .day { width: 60px; }
  .schedule-a { left: 77px; }
  .schedule-b { left: 296px; }
  .inquiry {
    position: absolute; left: 77px; top: 133px;
    font-size: 12.5px; font-weight: 400;
  }
  .inquiry b { font-weight: 700; font-size: 13.5px; }
</style>
</head>
<body>
  <div class="sheet-title">Post Card Design</div>
  <div class="sheet-size">Size : 139mm x 107mm</div>

  <section class="card-front">
    <div class="flag-photo" role="img" aria-label="Waving U.S. flag photograph in red, white and blue fading into black"></div>
    <div class="light-beam"></div>
    <div class="brand-mark"><span class="dot"></span>StudyBridgeAbroad</div>
    <div class="partner-mark"><span class="circle"></span>Federal Office of Exchange</div>
    <h1 class="tour-title">Off The Beaten Track Tour<br>(OTBT)</h1>
    <p class="tour-invite">Join us in VIETNAM</p>
    <p class="tour-dates">SEPTEMBER <b>29</b> – OCTOBER <b>03</b></p>
    <p class="tour-note">Registration is FREE &nbsp;|&nbsp; Space is limited</p>
    <p class="tour-signup">Sign up today at <b>go.example/OTBT_Vietnam</b></p>
  </section>

  <section class="card-back">
    <div class="back-band">
      <div class="band-flag" role="img" aria-label="Faint greyscale flag photograph"></div>
      <div class="band-content">
        <h2 class="save-title">Save the dates!</h2>
        <p class="save-lead">Spend one week visiting northern Vietnam's best gifted and talented high schools that are "off the beaten track" of most U.S. recruiters.</p>
        <p class="save-meta">Tour will originate from and return to Hanoi Transportation provided by Exchange Office</p>
      </div>
      <table class="schedule schedule-a">
        <tr><td class="day">Sept 29 (Mo)</td><td>: Hung Yen &amp; Nam Dinh Provinces</td></tr>
        <tr><td class="day">Sept 30 (Tu)</td><td>: Ninh Binh Province</td></tr>
        <tr><td class="day">Oct 1 (We)</td><td>: Thanh Hoa Province</td></tr>
      </table>
      <table class="schedule schedule-b">
        <tr><td class="day">Oct 2 (Th)</td><td>: Nghe An Province</td></tr>
        <tr><td class="day">Oct 3 (Fr)</td><td>: Thai Binh Province</td></tr>
      </table>
      <p class="inquiry">For Inquiries Email: <b>hanoi@studybridge.example</b></p>
    </div>
  </section>
</body>
</html>
```